Business Card Design Project

I would like a business card created for a new company. This is a holding company that acts as my investment company. It holds real estate and service based companies. The name of the company is Sandorecca which is Italian for Evolution. Defined as development or growth.
We currently have no logo. I really like some of the "different" cards out there. Potentially metallic or grey/black. That looks premium/hi-end and unique. I am not sure if your design would be specific to the card stock I end with our just logo/design/font.
Real Estate

```html
<!DOCTYPE html>
<html lang="en">
<head>
<meta charset="utf-8">
<title>Sandorecca — Business Card</title>
<link href="https://fonts.googleapis.com/css2?family=Archivo:wght@700&family=UnifrakturMaguntia&family=Lato:wght@400&display=swap" rel="stylesheet">
<style>
  :root {
    --backdrop: #ecebf2;
    --metal-dark: #8e8e8e;
    --metal-mid: #c4c4c4;
    --metal-light: #f4f4f4;
    --brush-line: rgba(255,255,255,0.18);
    --brush-shade: rgba(0,0,0,0.05);
    --ink: #141414;
    --ink-soft: #3a3a3a;
    --label-fill: rgba(255,255,255,0.55);
    --divider: #9a9a9a;
  }
  * { margin: 0; padding: 0; box-sizing: border-box; }
  html, body {
    width: 1200px; height: 900px; overflow: hidden;
    background: radial-gradient(ellipse at 50% 45%, #f7f7fb 0%, var(--backdrop) 70%);
  }
  .sheet {
    width: 1200px; height: 900px;
    display: flex; flex-direction: column;
    align-items: center; justify-content: center; gap: 60px;
  }
  .card {
    position: relative;
    width: 630px; height: 360px;
    border-radius: 6px;
    overflow: hidden;
    background:
      repeating-linear-gradient(0deg, var(--brush-line) 0 1px, transparent 1px 3px),
      repeating-linear-gradient(0deg, var(--brush-shade) 0 1px, transparent 1px 5px),
      linear-gradient(100deg, var(--metal-dark) 0%, var(--metal-light) 30%, var(--metal-mid) 48%, var(--metal-light) 66%, var(--metal-dark) 100%);
    box-shadow: 0 14px 30px rgba(0,0,0,0.18), 0 2px 4px rgba(0,0,0,0.12);
    display: flex; align-items: center; justify-content: center;
  }
  .card-front .wordmark-label {
    background: var(--label-fill);
    padding: 22px 34px;
  }
  .wordmark {
    font-family: "Archivo", "Arial", sans-serif;
    font-weight: 700;
    font-size: 52px;
    letter-spacing: 1px;
    text-transform: uppercase;
    color: var(--ink);
  }
  .card-back .details-label {
    display: flex; align-items: center; gap: 26px;
    background: var(--label-fill);
    padding: 22px 30px;
  }
  .holder { text-align: center; }
  .holder-name {
    font-family: "UnifrakturMaguntia", "Times New Roman", serif;
    font-size: 40px;
    color: var(--ink);
    line-height: 1;
  }
  .holder-role {
    font-family: "Lato", "Arial", sans-serif;
    font-size: 14px;
    color: var(--ink-soft);
    margin-top: 6px;
  }
  .divider { width: 1px; height: 80px; background: var(--divider); }
  .contact {
    list-style: none;
    font-family: "Lato", "Arial", sans-serif;
    font-size: 14px;
    line-height: 1.7;
    color: var(--ink-soft);
  }
</style>
</head>
<body>
  <main class="sheet">
    <section class="card card-front" aria-label="Card front">
      <div class="wordmark-label">
        <h1 class="wordmark">Sandorecca</h1>
      </div>
    </section>
    <section class="card card-back" aria-label="Card back">
      <div class="details-label">
        <div class="holder">
          <p class="holder-name">Marco Rinaldi</p>
          <p class="holder-role">Manager</p>
        </div>
        <span class="divider"></span>
        <ul class="contact">
          <li>phone: 555 019 284</li>
          <li>e-mail: marco@sandorecca-holding.com</li>
          <li>www.sandorecca-holding.com</li>
        </ul>
      </div>
    </section>
  </main>
</body>
</html>
```